Modern Attractive Letterhead for Veterinary House Call Business.

A letterhead which can be printed on A4, A5 and A6 paper sizes.
To have: ( our files to be uploaded)
1. Logo with Text
2. telephone
3. email
4. website
5. Address

Target Market(s)

60-85year mainly women pet owners. Also market include families, young professionals, busy people who have dogs and cats

Industry/Entity Type

Business

Requirements
Must have
• 1. Logo with Text ( provided)
• 2. telephone
• 3. email
• 4. website
• 5. Address
Nice to have
• Needs to be modern, preferably warm and caring in nature( if possible )
Should not have
• difficulty in printing A5 and A6

```html
<!DOCTYPE html>
<html lang="en">
<head>
<meta charset="utf-8">
<title>Hearth Pet Care – Letterhead Set</title>
<link href="https://fonts.googleapis.com/css2?family=Questrial&display=swap" rel="stylesheet">
<style>
  :root {
    --backdrop: #2b2b2d;
    --paper: #f4f4f4;
    --brand-blue: #2c7fb0;
    --brand-green: #5aa33a;
    --ink: #3a3a3a;
    --watermark-a: #e6e6e6;
    --watermark-b: #ececec;
  }
  * { box-sizing: border-box; margin: 0; padding: 0; }
  html, body {
    width: 1200px; height: 1000px; overflow: hidden;
    background: var(--backdrop);
    font-family: "Questrial", "Century Gothic", sans-serif;
  }
  .canvas { position: relative; width: 1200px; height: 1000px; }

  .sheet {
    position: absolute;
    background: var(--paper);
    overflow: hidden;
  }
  .sheet--a4 { left: 121px; top: 51px;  width: 510px; height: 719px; font-size: 10px; }
  .sheet--a5 { left: 720px; top: 51px;  width: 359px; height: 509px; font-size: 7px; }
  .sheet--a6 { left: 772px; top: 597px; width: 255px; height: 358px; font-size: 5px; }

  .brand {
    position: absolute;
    display: flex; align-items: center; gap: 0.5em;
    left: var(--brand-x); top: var(--brand-y);
  }
  .brand__mark {
    width: 1.6em; height: 1.6em;
    background: var(--brand-green);
  }
  .brand__name {
    font-size: 2em;
    color: var(--brand-blue);
    letter-spacing: 0.02em;
    white-space: nowrap;
  }

  .contact {
    position: absolute;
    left: var(--contact-x); top: var(--contact-y);
    font-size: 0.78em;
    line-height: 1.3;
    color: var(--ink);
  }
  .contact__row { display: flex; align-items: center; gap: 0.45em; white-space: nowrap; }
  .contact__icon {
    width: 1em; height: 1em; flex: none;
    background: var(--brand-blue); border-radius: 0.15em;
    display: flex; align-items: center; justify-content: center;
  }
  .contact__icon svg { width: 0.7em; height: 0.7em; }
  .contact__address { margin-top: 0.7em; }

  .sheet--a4 { --brand-x: 7.6%; --brand-y: 6.4%; --contact-x: 70.6%; --contact-y: 7.2%; }
  .sheet--a5 { --brand-x: 7%;   --brand-y: 7%;   --contact-x: 65%;   --contact-y: 7.3%; }
  .sheet--a6 { --brand-x: 11%;  --brand-y: 7.4%; --contact-x: 59%;   --contact-y: 7.8%; }

  .watermark {
    position: absolute;
    left: 0; bottom: 0;
    width: 88%; height: 49%;
    background: linear-gradient(160deg, var(--watermark-b), var(--watermark-a));
    border-radius: 55% 45% 0 0 / 35% 40% 0 0;
    opacity: 0.85;
  }
</style>
</head>
<body>
<main class="canvas">

  <section class="sheet sheet--a4" aria-label="A4 letterhead">
    <div class="watermark" role="img" aria-label="Faint large pet and house illustration"></div>
    <div class="brand"><span class="brand__mark"></span><span class="brand__name">Hearth Pet Care</span></div>
    <address class="contact">
      <div class="contact__row"><span class="contact__icon"><svg viewBox="0 0 10 10"><path d="M2 1h2l1 2-1.2 1a5 5 0 0 0 2.2 2.2L7 5l2 1v2a1 1 0 0 1-1 1A7 7 0 0 1 1 2a1 1 0 0 1 1-1z" fill="#fff"/></svg></span>0400 555 012</div>
      <div class="contact__row"><span class="contact__icon"><svg viewBox="0 0 10 10"><rect x="1" y="2.5" width="8" height="5" fill="none" stroke="#fff"/><path d="M1 2.5l4 3 4-3" fill="none" stroke="#fff"/></svg></span>hello@hearthpetcare.com.au</div>
      <div class="contact__row"><span class="contact__icon"><svg viewBox="0 0 10 10"><circle cx="5" cy="5" r="3.8" fill="none" stroke="#fff"/><path d="M1.2 5h7.6M5 1.2c-2 2.5-2 5 0 7.6M5 1.2c2 2.5 2 5 0 7.6" fill="none" stroke="#fff" stroke-width="0.7"/></svg></span>www.hearthpetcare.com.au</div>
      <div class="contact__address">PO Box 4410<br>Kenmore Hills QLD 4069</div>
    </address>
  </section>

  <section class="sheet sheet--a5" aria-label="A5 letterhead">
    <div class="watermark" role="img" aria-label="Faint large pet and house illustration"></div>
    <div class="brand"><span class="brand__mark"></span><span class="brand__name">Hearth Pet Care</span></div>
    <address class="contact">
      <div class="contact__row"><span class="contact__icon"><svg viewBox="0 0 10 10"><path d="M2 1h2l1 2-1.2 1a5 5 0 0 0 2.2 2.2L7 5l2 1v2a1 1 0 0 1-1 1A7 7 0 0 1 1 2a1 1 0 0 1 1-1z" fill="#fff"/></svg></span>0400 555 012</div>
      <div class="contact__row"><span class="contact__icon"><svg viewBox="0 0 10 10"><rect x="1" y="2.5" width="8" height="5" fill="none" stroke="#fff"/><path d="M1 2.5l4 3 4-3" fill="none" stroke="#fff"/></svg></span>hello@hearthpetcare.com.au</div>
      <div class="contact__row"><span class="contact__icon"><svg viewBox="0 0 10 10"><circle cx="5" cy="5" r="3.8" fill="none" stroke="#fff"/><path d="M1.2 5h7.6M5 1.2c-2 2.5-2 5 0 7.6M5 1.2c2 2.5 2 5 0 7.6" fill="none" stroke="#fff" stroke-width="0.7"/></svg></span>www.hearthpetcare.com.au</div>
      <div class="contact__address">PO Box 4410<br>Kenmore Hills QLD 4069</div>
    </address>
  </section>

  <section class="sheet sheet--a6" aria-label="A6 letterhead">
    <div class="watermark" role="img" aria-label="Faint large pet and house illustration"></div>
    <div class="brand"><span class="brand__mark"></span><span class="brand__name">Hearth Pet Care</span></div>
    <address class="contact">
      <div class="contact__row"><span class="contact__icon"><svg viewBox="0 0 10 10"><path d="M2 1h2l1 2-1.2 1a5 5 0 0 0 2.2 2.2L7 5l2 1v2a1 1 0 0 1-1 1A7 7 0 0 1 1 2a1 1 0 0 1 1-1z" fill="#fff"/></svg></span>0400 555 012</div>
      <div class="contact__row"><span class="contact__icon"><svg viewBox="0 0 10 10"><rect x="1" y="2.5" width="8" height="5" fill="none" stroke="#fff"/><path d="M1 2.5l4 3 4-3" fill="none" stroke="#fff"/></svg></span>hello@hearthpetcare.com.au</div>
      <div class="contact__row"><span class="contact__icon"><svg viewBox="0 0 10 10"><circle cx="5" cy="5" r="3.8" fill="none" stroke="#fff"/><path d="M1.2 5h7.6M5 1.2c-2 2.5-2 5 0 7.6M5 1.2c2 2.5 2 5 0 7.6" fill="none" stroke="#fff" stroke-width="0.7"/></svg></span>www.hearthpetcare.com.au</div>
      <div class="contact__address">PO Box 4410<br>Kenmore Hills QLD 4069</div>
    </address>
  </section>

</main>
</body>
</html>
```